Flyer for the Lumen 2025 Conference

I am looking to produce a flyer for our upcoming conference, Lumen 2025. This is an annual conference that we plan to publicize on social media. The ideal designer will create a flyer that is eye-catching and effectively communicates the key information. Please see attached our logo, speaker photo, and flyer content.

Target Market(s)

All demographics

Industry/Entity Type

Christian

Font styles to use
Sans Serif

Requirements
Should not have
• Cross, church

```html
<!DOCTYPE html>
<html lang="en">
<head>
<meta charset="utf-8">
<title>Lumen 2025 Conference</title>
<link rel="stylesheet" href="https://fonts.googleapis.com/css2?family=Allura&family=Bebas+Neue&family=Cinzel:wght@400;600&family=Oswald:wght@300;400;500&family=Righteous&display=swap">
<style>
  :root {
    --ink: #ffffff;
    --night: #0b1020;
    --deep-green: #0f5a45;
    --teal: #2a7f9a;
    --teal-dark: #123f57;
    --ember: #c2283a;
    --orange: #f7931e;
    --suit-blue: #1f5fae;
    --panel: #000000;
  }
  html, body { margin: 0; padding: 0; overflow: hidden; background: var(--night); }
  .flyer {
    position: relative;
    width: 960px; height: 1200px;
    overflow: hidden;
    color: var(--ink);
    font-family: "Oswald", sans-serif;
  }
  .backdrop {
    position: absolute; inset: 0;
    background:
      radial-gradient(ellipse 70% 40% at 55% 0%, rgba(30,140,95,.85), transparent 70%),
      radial-gradient(ellipse 40% 45% at 0% 45%, rgba(194,40,58,.55), transparent 70%),
      radial-gradient(ellipse 50% 30% at 60% 35%, rgba(180,200,210,.25), transparent 70%),
      linear-gradient(180deg, #0d3b36 0%, #0d1a2e 45%, #0a1226 100%);
  }
  .speaker-photo {
    position: absolute; left: 480px; top: 200px; width: 480px; height: 1000px;
    background:
      radial-gradient(ellipse 22% 12% at 48% 14%, rgba(120,80,55,.9), transparent 80%),
      linear-gradient(180deg, rgba(31,95,174,0) 0%, rgba(31,95,174,.85) 30%, #1a55a0 70%, #133f7a 100%);
  }
  .event-year {
    position: absolute; left: 83px; top: 90px;
    font-family: "Cinzel", serif; font-size: 26px; letter-spacing: 19px;
  }
  .brand-name {
    position: absolute; left: 736px; top: 72px;
    font-family: "Cinzel", serif; font-weight: 400; font-size: 56px; letter-spacing: 1px;
  }
  .headline {
    position: absolute; left: 68px; top: 206px; margin: 0;
    font-family: "Bebas Neue", sans-serif; font-weight: 400;
    font-size: 134px; line-height: 112px; letter-spacing: 1px;
  }
  .with-script {
    position: absolute; left: 74px; top: 420px;
    font-family: "Allura", cursive; font-size: 76px; line-height: 1;
  }
  .speaker-name {
    position: absolute; left: 200px; top: 452px; width: 362px; height: 44px;
    background: linear-gradient(90deg, var(--teal-dark), var(--teal));
    font-family: "Cinzel", serif; font-size: 25px; line-height: 44px;
    text-align: center;
  }
  .label {
    position: absolute; left: 72px;
    font-family: "Righteous", sans-serif; font-size: 26px; letter-spacing: 1px;
  }
  .topic-title {
    position: absolute; left: 72px; top: 588px;
    font-family: "Bebas Neue", sans-serif; font-size: 66px; color: var(--orange); line-height: 1;
  }
  .sessions { position: absolute; left: 71px; top: 731px; display: flex; gap: 6px; }
  .session {
    width: 128px; height: 110px; border: 4px solid var(--ink); background: var(--panel);
    text-align: center; padding-top: 20px; box-sizing: content-box; height: 90px;
  }
  .session .day { font-weight: 300; font-size: 22px; letter-spacing: 2px; line-height: 1; }
  .session .date { font-weight: 300; font-size: 13px; margin-top: 8px; }
  .session .time { font-family: "Bebas Neue", sans-serif; font-size: 21px; color: var(--orange); margin-top: 6px; }
  .venue {
    position: absolute; left: 71px; top: 931px; width: 460px; height: 100px;
    background: linear-gradient(180deg, var(--teal) 0%, rgba(18,63,87,.6) 60%, rgba(18,63,87,0) 100%);
    padding: 6px 9px; box-sizing: border-box;
    font-weight: 500; font-size: 23px; line-height: 31px; letter-spacing: 1px;
  }
  .app-note {
    position: absolute; left: 78px; top: 1132px;
    font-size: 19px; font-weight: 400;
  }
  .app-note .brand-inline { font-family: "Cinzel", serif; font-size: 21px; }
  .contact {
    position: absolute; right: 34px; top: 1086px; text-align: right;
    font-weight: 500; font-size: 26px; line-height: 36px;
  }
</style>
</head>
<body>
<main class="flyer">
  <div class="backdrop" role="img" aria-label="Abstract swirling background in green, red and deep navy light trails"></div>
  <div class="speaker-photo" role="img" aria-label="Photo of the speaker seated, wearing a blue suit and grey knit sweater"></div>

  <div class="event-year">LUMEN 2025</div>
  <div class="brand-name">VAREN</div>

  <h1 class="headline">PROPHETIC<br>CONFERENCE</h1>
  <div class="with-script">With</div>
  <div class="speaker-name">PROPHET ELIAS MWAMBA</div>

  <div class="label" style="top:545px">TOPIC</div>
  <div class="topic-title">VOICE OF THE LORD</div>

  <div class="label" style="top:683px">DATE/TIME</div>
  <div class="sessions">
    <div class="session"><div class="day">FRIDAY</div><div class="date">DECEMBER 26TH</div><div class="time">6:30PM - 9:00PM</div></div>
    <div class="session"><div class="day">SATURDAY</div><div class="date">DECEMBER 27TH</div><div class="time">5:30PM - 8:00PM</div></div>
    <div class="session"><div class="day">SUNDAY</div><div class="date">DECEMBER 28TH</div><div class="time">4:30PM - 7:00PM</div></div>
  </div>

  <div class="label" style="top:886px">LOCATION</div>
  <div class="venue">THE HARBOR HILL ARTS CENTER<br>218 LINDEN GROVE ROAD<br>FAIRHAVEN, MAINE 04117</div>

  <div class="app-note">DOWNLOAD THE <span class="brand-inline">VAREN</span> APP TO STAY UPDATED ON THE EVENT</div>

  <div class="contact">207 555 0142<br>HELLO@VAREN.ORG<br>WWW.VAREN.ORG</div>
</main>
</body>
</html>
```